Washing powder bag design.

Project Description – Graphic Design Proposal for ORNE Laundry Powder Packaging
We have already explored initial design ideas internally, supported by AI-assisted tools (ChatGPT) to develop early concepts, layouts, and mockups. To support this, we have attached the bag die-cut, where graphics and text are placed as a visual guideline for the intended structure. In addition, we have included a mockup of the product series currently under development to clearly communicate the desired style, direction, and overall visual identity.
The mockup should be regarded as the design foundation for this project and as a starting point for professional refinement.
Scope of Work
We would like you to create three graphic design variants, each based on a different color direction:
1. Variant 1: In line with our current color scheme
2. Variant 2: A blue version
3. Variant 3: A green version
Design Elements to Be Preserved
The following elements must be maintained across all three variants:
• The overall style and visual expression of the mockup
• The leaf-shaped element in the bottom right corner
• The ORNE layout, including typography, positioning, and general look & feel
Summary
While the color palette may vary, the structure, style, and key design elements must remain consistent and be directly based on the attached mockup.
We look forward to seeing your creative interpretation and professional input.
Updates
We need the design to be created based on the attached die-cut file “Orne 10 kg BAG 202526”, including all text elements.
We would like the final to include both the designed die-cut file and a mockup.

```html
<!DOCTYPE html>
<html lang="da">
<head>
<meta charset="utf-8">
<title>ORNE Vaskepulver – 10 kg bag artwork</title>
<link rel="stylesheet" href="https://fonts.googleapis.com/css2?family=Open+Sans:wght@400;600;700;800&family=Ubuntu:wght@500;700&display=swap">
<style>
  :root{
    --stage:#4a4a4a;
    --font-main:"Open Sans", Arial, sans-serif;
    --font-brand:"Ubuntu", "Open Sans", sans-serif;
  }
  *{box-sizing:border-box;margin:0;padding:0}
  html,body{width:1200px;height:3602px;overflow:hidden}
  body{background:var(--stage);font-family:var(--font-main);position:relative}

  .theme-blue{
    --bg:linear-gradient(180deg,#19a2ee 0%,#7fcdf5 20%,#f2fafe 45%,#e4f5fd 62%,#5cbcf0 85%,#1b9ded 100%);
    --ribbon:linear-gradient(180deg,#1a6fca,#1e8ee2);
    --box:#1c54a6; --box-text:#ffffff; --box-sub:#dbe9fb; --box-stitch:rgba(255,255,255,.85);
    --logo-fill:#ffffff; --logo-ring:#2a86d8; --logo-text:#1c54a6;
    --banner:#1c4f9a; --banner-text:#ffffff;
    --tag:#1c6fc4; --tag-text:#ffffff;
    --ink:#15509c; --side-ink:#1d3f6e;
    --warn:#1a72c8; --warn-text:#ffffff;
    --table-ink:#1d3f6e; --table-head:#1c55a8;
    --icon:#1c6fc4; --icon-cut:#ffffff;
    --leaf-a:rgba(176,222,92,.95); --leaf-b:rgba(92,160,48,.55);
    --stitch:rgba(255,255,255,.9);
  }
  .theme-cream{
    --bg:#fcf3e2;
    --ribbon:#d6dbb4;
    --box:#3f5b3f; --box-text:#ffffff; --box-sub:#e6ebd6; --box-stitch:rgba(255,255,255,.75);
    --logo-fill:#d6dbb4; --logo-ring:#eef0d8; --logo-text:#3f5b3f;
    --banner:#e8ecc4; --banner-text:#3f5b3f;
    --tag:#d6dbb4; --tag-text:#3f5b3f;
    --ink:#3f5b3f; --side-ink:#3f5b3f;
    --warn:#4f6b4c; --warn-text:#ffffff;
    --table-ink:#3f5b3f; --table-head:#4f6b4c;
    --icon:#3f5b3f; --icon-cut:#fcf3e2;
    --leaf-a:rgba(180,218,96,.95); --leaf-b:rgba(96,156,56,.5);
    --stitch:rgba(63,91,63,.7);
  }
  .theme-green{
    --bg:linear-gradient(180deg,#72bd44 0%,#5ba53e 45%,#2f7a3a 100%);
    --ribbon:linear-gradient(180deg,#24602e,#2f7036);
    --box:#ffffff; --box-text:#74b843; --box-sub:#2f6a34; --box-stitch:#a9c79a;
    --logo-fill:#ffffff; --logo-ring:#cfe7b8; --logo-text:#4e9a3a;
    --banner:#86c340; --banner-text:#ffffff;
    --tag:#3c8a3d; --tag-text:#ffffff;
    --ink:#ffffff; --side-ink:#ffffff;
    --warn:#7ab944; --warn-text:#ffffff;
    --table-ink:#2f5f2f; --table-head:#2f7036;
    --icon:#ffffff; --icon-cut:#3c8a3d;
    --leaf-a:rgba(206,236,130,.95); --leaf-b:rgba(90,150,50,.5);
    --stitch:rgba(255,255,255,.85);
  }

  /* flat die-cut panels */
  .dieline{position:absolute;left:183px;width:834px;height:685px;background:var(--bg);overflow:hidden;color:var(--ink)}
  .dieline--blue{top:1186px}
  .dieline--cream{top:1975px}
  .dieline--green{top:2797px}

  /* front composition, positioned in die-cut coordinates */
  .front{position:absolute;left:0;top:0;width:834px;height:685px}
  .ribbon{position:absolute;left:338px;top:0;width:165px;height:240px;background:var(--ribbon)}
  .ribbon::before,.ribbon::after{content:"";position:absolute;top:0;bottom:0;border-left:2px dashed var(--stitch)}
  .ribbon::before{left:12px}
  .ribbon::after{right:12px}

  .label-box{position:absolute;left:271px;top:229px;width:297px;height:207px;background:var(--box);border-radius:14px;box-shadow:0 6px 14px rgba(0,0,0,.18)}
  .label-box::before{content:"";position:absolute;inset:10px;border:2px dashed var(--box-stitch);border-radius:8px}
  .product-name{position:absolute;left:0;right:0;top:84px;text-align:center;font-family:var(--font-brand);font-weight:700;font-size:31px;line-height:36px;color:var(--box-text);letter-spacing:.5px}
  .product-sub{position:absolute;left:0;right:0;top:122px;text-align:center;font-size:16px;line-height:20px;font-weight:600;color:var(--box-sub)}

  .brand-mark{position:absolute;left:357px;top:171px;width:124px;height:124px;border-radius:50%;background:var(--logo-fill);border:6px solid var(--logo-ring);display:flex;align-items:center;justify-content:center;box-shadow:0 3px 8px rgba(0,0,0,.15)}
  .brand-name{font-family:var(--font-brand);font-weight:700;font-size:36px;color:var(--logo-text);letter-spacing:1px}

  .claim-banner{position:absolute;left:262px;top:394px;width:280px;height:34px;background:var(--banner);color:var(--banner-text);transform:rotate(-6deg);display:flex;align-items:center;justify-content:center;font-weight:700;font-size:14px;letter-spacing:.3px;border-radius:3px;box-shadow:0 3px 6px rgba(0,0,0,.15);white-space:nowrap}

  .weight-tag{position:absolute;left:325px;top:450px;width:70px;height:28px;background:var(--tag);color:var(--tag-text);transform:skewX(-12deg) rotate(-4deg);display:flex;align-items:center;justify-content:center;font-weight:700;font-size:14px;border-radius:3px}

  .care-row{position:absolute;display:flex;gap:6px;align-items:center}
  .front .care-row{left:313px;top:496px}
  .dose-badge{width:40px;height:30px;border-radius:6px;background:var(--icon);color:var(--icon-cut);display:flex;align-items:center;justify-content:center;font-weight:700;font-size:16px}
  .care-icon{width:32px;height:30px}
  .temps{position:absolute;font-size:11px;font-weight:600;color:var(--ink);white-space:nowrap}
  .front .temps{left:292px;top:535px}

  /* illustrated leaf sprigs: soft colour areas */
  .leaf-art{position:absolute;background:radial-gradient(ellipse at 50% 50%,var(--leaf-a) 0%,var(--leaf-b) 45%,transparent 72%)}
  .leaf-art--left{left:258px;top:146px;width:96px;height:86px}
  .leaf-art--top{left:474px;top:136px;width:92px;height:90px}
  .leaf-art--corner{left:446px;top:446px;width:120px;height:130px}

  /* left side panel */
  .warning{position:absolute;left:27px;top:101px;width:151px;height:238px;background:var(--warn);color:var(--warn-text);border-radius:4px 22px 4px 4px;padding:7px 7px;overflow:hidden}
  .warning-head{display:flex;align-items:center;gap:6px;font-size:9.5px;font-weight:700;padding-bottom:5px;border-bottom:1px solid rgba(255,255,255,.5);margin-bottom:5px}
  .warning-head svg{width:17px;height:15px;flex:none}
  .warning p{font-size:5.6px;line-height:1.42;margin-bottom:3px}
  .warning b{font-weight:800}

  .dosage{position:absolute;left:27px;top:346px;width:182px;border-collapse:collapse;background:#fff;color:var(--table-ink);font-size:7px}
  .dosage caption{background:var(--table-head);color:#fff;font-weight:700;font-size:9.5px;text-align:left;padding:2px 6px}
  .dosage th,.dosage td{border:1px solid #b8c2cc;padding:1px 3px;text-align:left;font-weight:600;white-space:nowrap}
  .dosage td:first-child{font-weight:800}
  .dosage .foot td{text-align:center;font-weight:600}

  .side-left .care-row{left:62px;top:496px}
  .side-left .temps{left:48px;top:535px}

  /* right side panel */
  .info-column{position:absolute;left:662px;top:132px;width:146px;font-size:5.5px;line-height:1.38;color:var(--side-ink)}
  .info-column p{margin-bottom:4px}
  .info-column b{font-weight:800}
  .producer{position:absolute;left:568px;top:415px;width:86px;height:119px;background:#fff;border:1px solid #c7ced6;color:#222;text-align:center;padding:6px 4px;font-size:5.6px;line-height:1.4}
  .producer-name{font-weight:800;font-size:14px;color:#222;margin:3px 0}
  .producer-weight{font-size:11px;font-weight:700;margin-top:4px}
  .producer-code{font-size:4.6px;margin-top:2px}

  /* flat bag front */
  .hero-front{position:absolute;left:370px;top:112px;width:460px;height:860px;background:var(--bg);overflow:hidden;color:var(--ink)}
  .hero-ribbon{position:absolute;left:122px;top:0;width:215px;height:350px;background:var(--ribbon)}
  .hero-ribbon::before,.hero-ribbon::after{content:"";position:absolute;top:0;bottom:0;border-left:2px dashed var(--stitch)}
  .hero-ribbon::before{left:15px}
  .hero-ribbon::after{right:15px}
  .hand-holes{position:absolute;left:152px;top:22px;display:flex;gap:24px}
  .hand-holes span{width:36px;height:36px;border-radius:50%;background:var(--stage)}
  .hero-front .front{transform:translate(-315px,44px) scale(1.3);transform-origin:0 0}
  .hero-front .ribbon{display:none}
</style>
</head>
<body>

<section class="hero-front theme-blue" aria-label="ORNE Vaskepulver bag front">
  <div class="hero-ribbon"></div>
  <div class="hand-holes"><span></span><span></span><span></span></div>
  <div class="front">
    <div class="leaf-art leaf-art--left" role="img" aria-label="Illustrated sprig of fresh green leaves"></div>
    <div class="leaf-art leaf-art--top" role="img" aria-label="Illustrated sprig of fresh green leaves"></div>
    <div class="label-box"><div class="product-name">VASKEPULVER</div><div class="product-sub">Laundry Detergent</div></div>
    <div class="brand-mark"><span class="brand-name">ORNE</span></div>
    <div class="claim-banner">LIV OG BALANCE | HVERDAGEN</div>
    <div class="weight-tag">10 KG</div>
    <div class="care-row">
      <div class="dose-badge">120</div>
      <svg class="care-icon" viewBox="0 0 32 30"><path d="M3 11h26l-3 15H6z" fill="none" stroke="var(--icon)" stroke-width="3"/><circle cx="11" cy="6" r="3" fill="var(--icon)"/><circle cx="21" cy="5" r="2" fill="var(--icon)"/></svg>
      <svg class="care-icon" viewBox="0 0 32 30"><rect x="2" y="1" width="28" height="28" rx="3" fill="var(--icon)"/><circle cx="16" cy="17" r="8" fill="var(--icon-cut)"/><rect x="5" y="4" width="8" height="3" fill="var(--icon-cut)"/></svg>
    </div>
    <div class="temps">20°C | 30°C | 40°C | 60°C | 90°C</div>
    <div class="leaf-art leaf-art--corner" role="img" aria-label="Illustrated branch of fresh green leaves"></div>
  </div>
</section>

<section class="dieline dieline--blue theme-blue" aria-label="Blue die-cut artwork">
  <div class="side-left">
    <div class="warning">
      <div class="warning-head"><svg viewBox="0 0 18 16"><path d="M9 1L17 15H1z" fill="#fff"/><path d="M9 6v4M9 12v1" stroke="#d62b2b" stroke-width="2"/></svg>Advarsel Warning</div>
      <p><b>[DK] Forårsager alvorlig øjenirritation.</b> Indeholder subtilisin, amylase, lipase, parfume. Kan udløse allergisk reaktion.</p>
      <p>Opbevares utilgængeligt for børn. Vask hænderne grundigt efter brug. Bær øjenbeskyttelse.</p>
      <p><b>VED KONTAKT MED ØJNENE:</b> Skyl forsigtigt med vand i flere minutter. Fjern eventuelle kontaktlinser, hvis dette kan gøres let. Fortsæt skylning. Ved vedvarende øjenirritation: Søg lægehjælp.</p>
      <p><b>[EN] Causes serious eye irritation.</b> Contains subtilisin, amylase, lipase, perfume. May produce an allergic reaction. Keep out of reach of children. Wash hands thoroughly after handling. Wear eye protection.</p>
      <p><b>IF IN EYES:</b> Rinse cautiously with water for several minutes. Remove contact lenses, if present and easy to do. Continue rinsing. If eye irritation persists: Get medical advice.</p>
      <p><b>UFI: 0000-0000-0000-0000</b></p>
    </div>
    <table class="dosage">
      <caption>DOSERING DOSAGE</caption>
      <tr><th></th><th>Blød. Soft</th><th>Medium</th><th>Hard</th></tr>
      <tr><td>1 KG</td><td>37 ml = 41 g</td><td>37 ml = 61 g</td><td>83 g</td></tr>
      <tr><td>5 KG</td><td>75 KG</td><td>75 ml = 83 g</td><td>83 g</td></tr>
      <tr><td>10 KG</td><td>112 Kg</td><td>112 ml = 124 g</td><td>144 g</td></tr>
      <tr class="foot"><td colspan="4">75 ml = 83 g</td></tr>
    </table>
    <div class="care-row">
      <div class="dose-badge">120</div>
      <svg class="care-icon" viewBox="0 0 32 30"><path d="M3 11h26l-3 15H6z" fill="none" stroke="var(--icon)" stroke-width="3"/><circle cx="11" cy="6" r="3" fill="var(--icon)"/><circle cx="21" cy="5" r="2" fill="var(--icon)"/></svg>
      <svg class="care-icon" viewBox="0 0 32 30"><rect x="2" y="1" width="28" height="28" rx="3" fill="var(--icon)"/><circle cx="16" cy="17" r="8" fill="var(--icon-cut)"/><rect x="5" y="4" width="8" height="3" fill="var(--icon-cut)"/></svg>
    </div>
    <div class="temps">20°C | 30°C | 40°C | 60°C | 90°C</div>
  </div>
  <div class="front">
    <div class="ribbon"></div>
    <div class="leaf-art leaf-art--left" role="img" aria-label="Illustrated sprig of fresh green leaves"></div>
    <div class="leaf-art leaf-art--top" role="img" aria-label="Illustrated sprig of fresh green leaves"></div>
    <div class="label-box"><div class="product-name">VASKEPULVER</div><div class="product-sub">Laundry Detergent</div></div>
    <div class="brand-mark"><span class="brand-name">ORNE</span></div>
    <div class="claim-banner">LIV OG BALANCE | HVERDAGEN</div>
    <div class="weight-tag">10 KG</div>
    <div class="care-row">
      <div class="dose-badge">120</div>
      <svg class="care-icon" viewBox="0 0 32 30"><path d="M3 11h26l-3 15H6z" fill="none" stroke="var(--icon)" stroke-width="3"/><circle cx="11" cy="6" r="3" fill="var(--icon)"/><circle cx="21" cy="5" r="2" fill="var(--icon)"/></svg>
      <svg class="care-icon" viewBox="0 0 32 30"><rect x="2" y="1" width="28" height="28" rx="3" fill="var(--icon)"/><circle cx="16" cy="17" r="8" fill="var(--icon-cut)"/><rect x="5" y="4" width="8" height="3" fill="var(--icon-cut)"/></svg>
    </div>
    <div class="temps">20°C | 30°C | 40°C | 60°C | 90°C</div>
    <div class="leaf-art leaf-art--corner" role="img" aria-label="Illustrated branch of fresh green leaves"></div>
  </div>
  <div class="producer">
    Produceret i EU for
    <div class="producer-name">KLARVIG</div>
    Nordvej 12<br>4000 Nordby<br>+45 00 00 00 00<br>info@klarvig.dk<br>www.klarvig.dk
    <div class="producer-weight">10kg</div>
    <div class="producer-code">LOT 000000 · BF 00.00</div>
  </div>
  <div class="info-column">
    <p><b>[DK] BRUGSANVISNING –</b> ORNE VASKEPULVER til universel brug. Egnet til alle typer vaskemaskiner og alle vasketemperaturer fra 20°C til 90°C. Sorter tøjet efter farve og materiale, og følg altid vaskeanvisningen i tøjet. Dosér efter vandets hårdhed, mængden af tøj og graden af snavs. Hæld pulveret direkte i doseringsrummet.</p>
    <p><b>ANBEFALINGER:</b> • Undgå overdosering – det belaster miljøet. • Ved meget snavset tøj kan dosis øges. • Ved sarte stoffer vælges et skånsomt program.</p>
    <p><b>OPBEVARING:</b> Opbevares tørt og lukket. Beskyt mod fugt. Må ikke udsættes for direkte sollys. Opbevares utilgængeligt for børn.</p>
    <p><b>SIKKERHED:</b> Forårsager alvorlig øjenirritation. Vask hænder efter brug. Ved kontakt med øjnene skylles grundigt med vand.</p>
    <p><b>[EN] DIRECTIONS –</b> ORNE LAUNDRY DETERGENT POWDER for universal use. Suitable for all types of washing machines and all temperatures from 20°C to 90°C. Sort laundry by colour and fabric and always follow the care label. Dose according to water hardness, load size and level of soiling.</p>
    <p><b>RECOMMENDATIONS:</b> • Avoid overdosing – it burdens the environment. • For heavily soiled laundry, increase the dose. • For delicate fabrics, use a gentle programme.</p>
    <p><b>STORAGE:</b> Store in a dry place with the bag tightly closed. Protect from moisture and direct sunlight. Keep out of reach of children.</p>
    <p><b>SAFETY:</b> Causes serious eye irritation. Wash hands after use.</p>
    <p><b>IF IN EYES:</b> Rinse cautiously with water for several minutes.</p>
    <p><b>INGREDIENTS (EC 648/2004):</b> 15–30% zeolites, 5–15% anionic surfactants, &lt;5% non-ionic surfactants, polycarboxylates, enzymes, optical brighteners, perfume.</p>
  </div>
</section>

<section class="dieline dieline--cream theme-cream" aria-label="Cream die-cut artwork">
  <div class="side-left">
    <div class="warning">
      <div class="warning-head"><svg viewBox="0 0 18 16"><path d="M9 1L17 15H1z" fill="#fff"/><path d="M9 6v4M9 12v1" stroke="#d62b2b" stroke-width="2"/></svg>Advarsel Warning</div>
      <p><b>[DK] Forårsager alvorlig øjenirritation.</b> Indeholder subtilisin, amylase, lipase, parfume. Kan udløse allergisk reaktion.</p>
      <p>Opbevares utilgængeligt for børn. Vask hænderne grundigt efter brug. Bær øjenbeskyttelse.</p>
      <p><b>VED KONTAKT MED ØJNENE:</b> Skyl forsigtigt med vand i flere minutter. Fjern eventuelle kontaktlinser, hvis dette kan gøres let. Fortsæt skylning. Ved vedvarende øjenirritation: Søg lægehjælp.</p>
      <p><b>[EN] Causes serious eye irritation.</b> Contains subtilisin, amylase, lipase, perfume. May produce an allergic reaction. Keep out of reach of children. Wash hands thoroughly after handling. Wear eye protection.</p>
      <p><b>IF IN EYES:</b> Rinse cautiously with water for several minutes. Remove contact lenses, if present and easy to do. Continue rinsing. If eye irritation persists: Get medical advice.</p>
      <p><b>UFI: 0000-0000-0000-0000</b></p>
    </div>
    <table class="dosage">
      <caption>DOSERING DOSAGE</caption>
      <tr><th></th><th>Blød. Soft</th><th>Medium</th><th>Hard</th></tr>
      <tr><td>1 KG</td><td>37 ml = 41 g</td><td>37 ml = 61 g</td><td>83 g</td></tr>
      <tr><td>5 KG</td><td>75 KG</td><td>75 ml = 83 g</td><td>83 g</td></tr>
      <tr><td>10 KG</td><td>112 Kg</td><td>112 ml = 124 g</td><td>144 g</td></tr>
      <tr class="foot"><td colspan="4">75 ml = 83 g</td></tr>
    </table>
    <div class="care-row">
      <div class="dose-badge">120</div>
      <svg class="care-icon" viewBox="0 0 32 30"><path d="M3 11h26l-3 15H6z" fill="none" stroke="var(--icon)" stroke-width="3"/><circle cx="11" cy="6" r="3" fill="var(--icon)"/><circle cx="21" cy="5" r="2" fill="var(--icon)"/></svg>
      <svg class="care-icon" viewBox="0 0 32 30"><rect x="2" y="1" width="28" height="28" rx="3" fill="var(--icon)"/><circle cx="16" cy="17" r="8" fill="var(--icon-cut)"/><rect x="5" y="4" width="8" height="3" fill="var(--icon-cut)"/></svg>
    </div>
    <div class="temps">20°C | 30°C | 40°C | 60°C | 90°C</div>
  </div>
  <div class="front">
    <div class="ribbon"></div>
    <div class="leaf-art leaf-art--left" role="img" aria-label="Illustrated sprig of fresh green leaves"></div>
    <div class="leaf-art leaf-art--top" role="img" aria-label="Illustrated sprig of fresh green leaves"></div>
    <div class="label-box"><div class="product-name">VASKEPULVER</div><div class="product-sub">Laundry Detergent</div></div>
    <div class="brand-mark"><span class="brand-name">ORNE</span></div>
    <div class="claim-banner">LIV OG BALANCE | HVERDAGEN</div>
    <div class="weight-tag">10 KG</div>
    <div class="care-row">
      <div class="dose-badge">120</div>
      <svg class="care-icon" viewBox="0 0 32 30"><path d="M3 11h26l-3 15H6z" fill="none" stroke="var(--icon)" stroke-width="3"/><circle cx="11" cy="6" r="3" fill="var(--icon)"/><circle cx="21" cy="5" r="2" fill="var(--icon)"/></svg>
      <svg class="care-icon" viewBox="0 0 32 30"><rect x="2" y="1" width="28" height="28" rx="3" fill="var(--icon)"/><circle cx="16" cy="17" r="8" fill="var(--icon-cut)"/><rect x="5" y="4" width="8" height="3" fill="var(--icon-cut)"/></svg>
    </div>
    <div class="temps">20°C | 30°C | 40°C | 60°C | 90°C</div>
    <div class="leaf-art leaf-art--corner" role="img" aria-label="Illustrated branch of fresh green leaves"></div>
  </div>
  <div class="producer">
    Produceret i EU for
    <div class="producer-name">KLARVIG</div>
    Nordvej 12<br>4000 Nordby<br>+45 00 00 00 00<br>info@klarvig.dk<br>www.klarvig.dk
    <div class="producer-weight">10kg</div>
    <div class="producer-code">LOT 000000 · BF 00.00</div>
  </div>
  <div class="info-column">
    <p><b>[DK] BRUGSANVISNING –</b> ORNE VASKEPULVER til universel brug. Egnet til alle typer vaskemaskiner og alle vasketemperaturer fra 20°C til 90°C. Sorter tøjet efter farve og materiale, og følg altid vaskeanvisningen i tøjet. Dosér efter vandets hårdhed, mængden af tøj og graden af snavs. Hæld pulveret direkte i doseringsrummet.</p>
    <p><b>ANBEFALINGER:</b> • Undgå overdosering – det belaster miljøet. • Ved meget snavset tøj kan dosis øges. • Ved sarte stoffer vælges et skånsomt program.</p>
    <p><b>OPBEVARING:</b> Opbevares tørt og lukket. Beskyt mod fugt. Må ikke udsættes for direkte sollys. Opbevares utilgængeligt for børn.</p>
    <p><b>SIKKERHED:</b> Forårsager alvorlig øjenirritation. Vask hænder efter brug. Ved kontakt med øjnene skylles grundigt med vand.</p>
    <p><b>[EN] DIRECTIONS –</b> ORNE LAUNDRY DETERGENT POWDER for universal use. Suitable for all types of washing machines and all temperatures from 20°C to 90°C. Sort laundry by colour and fabric and always follow the care label. Dose according to water hardness, load size and level of soiling.</p>
    <p><b>RECOMMENDATIONS:</b> • Avoid overdosing – it burdens the environment. • For heavily soiled laundry, increase the dose. • For delicate fabrics, use a gentle programme.</p>
    <p><b>STORAGE:</b> Store in a dry place with the bag tightly closed. Protect from moisture and direct sunlight. Keep out of reach of children.</p>
    <p><b>SAFETY:</b> Causes serious eye irritation. Wash hands after use.</p>
    <p><b>IF IN EYES:</b> Rinse cautiously with water for several minutes.</p>
    <p><b>INGREDIENTS (EC 648/2004):</b> 15–30% zeolites, 5–15% anionic surfactants, &lt;5% non-ionic surfactants, polycarboxylates, enzymes, optical brighteners, perfume.</p>
  </div>
</section>

<section class="dieline dieline--green theme-green" aria-label="Green die-cut artwork">
  <div class="side-left">
    <div class="warning">
      <div class="warning-head"><svg viewBox="0 0 18 16"><path d="M9 1L17 15H1z" fill="#fff"/><path d="M9 6v4M9 12v1" stroke="#d62b2b" stroke-width="2"/></svg>Advarsel Warning</div>
      <p><b>[DK] Forårsager alvorlig øjenirritation.</b> Indeholder subtilisin, amylase, lipase, parfume. Kan udløse allergisk reaktion.</p>
      <p>Opbevares utilgængeligt for børn. Vask hænderne grundigt efter brug. Bær øjenbeskyttelse.</p>
      <p><b>VED KONTAKT MED ØJNENE:</b> Skyl forsigtigt med vand i flere minutter. Fjern eventuelle kontaktlinser, hvis dette kan gøres let. Fortsæt skylning. Ved vedvarende øjenirritation: Søg lægehjælp.</p>
      <p><b>[EN] Causes serious eye irritation.</b> Contains subtilisin, amylase, lipase, perfume. May produce an allergic reaction. Keep out of reach of children. Wash hands thoroughly after handling. Wear eye protection.</p>
      <p><b>IF IN EYES:</b> Rinse cautiously with water for several minutes. Remove contact lenses, if present and easy to do. Continue rinsing. If eye irritation persists: Get medical advice.</p>
      <p><b>UFI: 0000-0000-0000-0000</b></p>
    </div>
    <table class="dosage">
      <caption>DOSERING DOSAGE</caption>
      <tr><th></th><th>Blød. Soft</th><th>Medium</th><th>Hard</th></tr>
      <tr><td>1 KG</td><td>37 ml = 41 g</td><td>37 ml = 61 g</td><td>83 g</td></tr>
      <tr><td>5 KG</td><td>75 KG</td><td>75 ml = 83 g</td><td>83 g</td></tr>
      <tr><td>10 KG</td><td>112 Kg</td><td>112 ml = 124 g</td><td>144 g</td></tr>
      <tr class="foot"><td colspan="4">75 ml = 83 g</td></tr>
    </table>
    <div class="care-row">
      <div class="dose-badge">120</div>
      <svg class="care-icon" viewBox="0 0 32 30"><path d="M3 11h26l-3 15H6z" fill="none" stroke="var(--icon)" stroke-width="3"/><circle cx="11" cy="6" r="3" fill="var(--icon)"/><circle cx="21" cy="5" r="2" fill="var(--icon)"/></svg>
      <svg class="care-icon" viewBox="0 0 32 30"><rect x="2" y="1" width="28" height="28" rx="3" fill="var(--icon)"/><circle cx="16" cy="17" r="8" fill="var(--icon-cut)"/><rect x="5" y="4" width="8" height="3" fill="var(--icon-cut)"/></svg>
    </div>
    <div class="temps">20°C | 30°C | 40°C | 60°C | 90°C</div>
  </div>
  <div class="front">
    <div class="ribbon"></div>
    <div class="leaf-art leaf-art--left" role="img" aria-label="Illustrated sprig of fresh green leaves"></div>
    <div class="leaf-art leaf-art--top" role="img" aria-label="Illustrated sprig of fresh green leaves"></div>
    <div class="label-box"><div class="product-name">VASKEPULVER</div><div class="product-sub">Laundry Detergent</div></div>
    <div class="brand-mark"><span class="brand-name">ORNE</span></div>
    <div class="claim-banner">LIV OG BALANCE | HVERDAGEN</div>
    <div class="weight-tag">10 KG</div>
    <div class="care-row">
      <div class="dose-badge">120</div>
      <svg class="care-icon" viewBox="0 0 32 30"><path d="M3 11h26l-3 15H6z" fill="none" stroke="var(--icon)" stroke-width="3"/><circle cx="11" cy="6" r="3" fill="var(--icon)"/><circle cx="21" cy="5" r="2" fill="var(--icon)"/></svg>
      <svg class="care-icon" viewBox="0 0 32 30"><rect x="2" y="1" width="28" height="28" rx="3" fill="var(--icon)"/><circle cx="16" cy="17" r="8" fill="var(--icon-cut)"/><rect x="5" y="4" width="8" height="3" fill="var(--icon-cut)"/></svg>
    </div>
    <div class="temps">20°C | 30°C | 40°C | 60°C | 90°C</div>
    <div class="leaf-art leaf-art--corner" role="img" aria-label="Illustrated branch of fresh green leaves"></div>
  </div>
  <div class="producer">
    Produceret i EU for
    <div class="producer-name">KLARVIG</div>
    Nordvej 12<br>4000 Nordby<br>+45 00 00 00 00<br>info@klarvig.dk<br>www.klarvig.dk
    <div class="producer-weight">10kg</div>
    <div class="producer-code">LOT 000000 · BF 00.00</div>
  </div>
  <div class="info-column">
    <p><b>[DK] BRUGSANVISNING –</b> ORNE VASKEPULVER til universel brug. Egnet til alle typer vaskemaskiner og alle vasketemperaturer fra 20°C til 90°C. Sorter tøjet efter farve og materiale, og følg altid vaskeanvisningen i tøjet. Dosér efter vandets hårdhed, mængden af tøj og graden af snavs. Hæld pulveret direkte i doseringsrummet.</p>
    <p><b>ANBEFALINGER:</b> • Undgå overdosering – det belaster miljøet. • Ved meget snavset tøj kan dosis øges. • Ved sarte stoffer vælges et skånsomt program.</p>
    <p><b>OPBEVARING:</b> Opbevares tørt og lukket. Beskyt mod fugt. Må ikke udsættes for direkte sollys. Opbevares utilgængeligt for børn.</p>
    <p><b>SIKKERHED:</b> Forårsager alvorlig øjenirritation. Vask hænder efter brug. Ved kontakt med øjnene skylles grundigt med vand.</p>
    <p><b>[EN] DIRECTIONS –</b> ORNE LAUNDRY DETERGENT POWDER for universal use. Suitable for all types of washing machines and all temperatures from 20°C to 90°C. Sort laundry by colour and fabric and always follow the care label. Dose according to water hardness, load size and level of soiling.</p>
    <p><b>RECOMMENDATIONS:</b> • Avoid overdosing – it burdens the environment. • For heavily soiled laundry, increase the dose. • For delicate fabrics, use a gentle programme.</p>
    <p><b>STORAGE:</b> Store in a dry place with the bag tightly closed. Protect from moisture and direct sunlight. Keep out of reach of children.</p>
    <p><b>SAFETY:</b> Causes serious eye irritation. Wash hands after use.</p>
    <p><b>IF IN EYES:</b> Rinse cautiously with water for several minutes.</p>
    <p><b>INGREDIENTS (EC 648/2004):</b> 15–30% zeolites, 5–15% anionic surfactants, &lt;5% non-ionic surfactants, polycarboxylates, enzymes, optical brighteners, perfume.</p>
  </div>
</section>

</body>
</html>
```